E-Blast with US football theme

Hello, we are looking for an email blast with a US football theme (Grand Clash in the US is next weekend).
Specs:
600px w x 1500px h
Headline: Need Financing For A Win?
Winning teams donβt leave success to chanceβthey build a solid game plan.
Whether youβre expanding, constructing, refinancing, or making key acquisitions, RVB provides financing solutions that help you execute your strategy with confidence. Letβs work together to create a winning playbook.
Our custom financing solutions include:
π Acquisitions
π Construction
π Refinancing
π Recapitalizations
π Structured Leases
And our products include:
π Bridge
π Mezzanine
π Unitranche
π NNN Lease
π Preferred Equity
Look and feel
Each slider illustrates characteristics of the customer's brand and the style your logo design should communicate.

```html
<!DOCTYPE html>
<html lang="en">
<head>
<meta charset="utf-8">
<title>Need Financing For A Win? – RVB E-Blast</title>
<link href="https://fonts.googleapis.com/css2?family=Barlow+Condensed:ital,wght@0,500;0,600;0,700;1,600&family=Orbitron:wght@900&display=swap" rel="stylesheet">
<style>
  :root {
    --stage: #a9a9a9;
    --navy-deep: #0a1636;
    --navy: #12255e;
    --royal: #1556b0;
    --sky: #4bc3ef;
    --band: #081628;
    --white: #ffffff;
    --brand: #27357f;
  }
  * { margin: 0; padding: 0; box-sizing: border-box; }
  html, body {
    width: 1200px; height: 1200px; overflow: hidden;
    background: var(--stage);
  }
  .eblast {
    position: absolute; left: 420px; top: 148px;
    width: 360px; height: 899px;
    background: var(--white);
    font-family: "Barlow Condensed", sans-serif;
    color: var(--white);
  }
  .hero {
    position: absolute; left: 0; top: 0; width: 360px; height: 751px;
    overflow: hidden;
    background:
      radial-gradient(ellipse 70% 35% at 25% 20%, rgba(40,130,230,.75), transparent 70%),
      radial-gradient(ellipse 80% 40% at 45% 60%, rgba(20,90,190,.8), transparent 70%),
      linear-gradient(180deg, #1b2c72 0%, #102a6e 40%, #0b2a6a 65%, var(--navy-deep) 100%);
  }
  .hero-photo {
    position: absolute; left: 102px; top: 200px; width: 258px; height: 551px;
    background:
      radial-gradient(ellipse 40% 30% at 70% 60%, rgba(10,20,50,.85), transparent 75%),
      radial-gradient(ellipse 50% 25% at 55% 90%, rgba(8,14,36,.9), transparent 75%),
      linear-gradient(160deg, transparent 20%, rgba(40,120,220,.35) 60%, rgba(10,20,50,.6) 100%);
  }
  .headline {
    position: absolute; left: 28px; top: 44px;
    font-family: "Orbitron", sans-serif; font-weight: 900;
    font-size: 36px; line-height: 41px; letter-spacing: 0.5px;
    color: var(--sky); text-transform: uppercase;
    transform: skewX(-10deg); transform-origin: left top;
  }
  .tagline {
    position: absolute; left: 32px; top: 174px; width: 300px;
    font-style: italic; font-weight: 600; font-size: 19.5px; line-height: 26px;
    letter-spacing: -0.3px;
  }
  .intro {
    position: absolute; left: 32px; top: 236px; width: 230px;
    font-weight: 500; font-size: 13.6px; line-height: 17.4px;
  }
  .band {
    position: absolute; left: 0; width: 253px; height: 25px;
    background: var(--band);
    clip-path: polygon(0 0, 100% 0, 96% 100%, 0 100%);
    color: var(--sky); font-weight: 600; font-size: 13px;
    line-height: 25px; padding-left: 32px;
  }
  .band-solutions { top: 343px; }
  .band-products { top: 510px; }
  .checklist {
    position: absolute; left: 45px; list-style: none;
    font-weight: 500; font-size: 13.6px; line-height: 23.3px;
  }
  .checklist li { display: flex; align-items: center; gap: 5px; }
  .checklist svg { width: 12px; height: 12px; flex: none; }
  .list-solutions { top: 373px; }
  .list-products { top: 540px; }
  .brand-footer {
    position: absolute; left: 0; top: 751px; width: 360px; height: 148px;
    display: flex; align-items: center; justify-content: center; gap: 10px;
  }
  .brand-square { width: 22px; height: 22px; background: var(--brand); }
  .brand-name {
    font-family: "Barlow Condensed", sans-serif; font-weight: 700;
    font-size: 40px; color: var(--brand); letter-spacing: 1px;
  }
</style>
</head>
<body>
  <main class="eblast">
    <section class="hero">
      <div class="hero-photo" role="img" aria-label="Football player in a dark blue uniform leaping and holding a football high overhead"></div>

      <h1 class="headline">Need<br>Financing<br>For a Win?</h1>

      <p class="tagline">Winning teams don’t leave success to chance —they build a solid game plan.</p>

      <p class="intro">Whether you’re expanding, constructing, refinancing, or making key acquisitions, RVB provides financing solutions that help you execute your strategy with confidence. Let’s work together to create a winning playbook.</p>

      <div class="band band-solutions">Our custom financing solutions include:</div>
      <ul class="checklist list-solutions">
        <li><svg viewBox="0 0 12 12"><ellipse cx="6" cy="6" rx="5.5" ry="3.4" transform="rotate(-40 6 6)" fill="none" stroke="var(--sky)" stroke-width="1"/><path d="M4 8 L8 4" stroke="var(--sky)" stroke-width="0.9"/></svg>Acquisitions</li>
        <li><svg viewBox="0 0 12 12"><ellipse cx="6" cy="6" rx="5.5" ry="3.4" transform="rotate(-40 6 6)" fill="none" stroke="var(--sky)" stroke-width="1"/><path d="M4 8 L8 4" stroke="var(--sky)" stroke-width="0.9"/></svg>Construction</li>
        <li><svg viewBox="0 0 12 12"><ellipse cx="6" cy="6" rx="5.5" ry="3.4" transform="rotate(-40 6 6)" fill="none" stroke="var(--sky)" stroke-width="1"/><path d="M4 8 L8 4" stroke="var(--sky)" stroke-width="0.9"/></svg>Refinancing</li>
        <li><svg viewBox="0 0 12 12"><ellipse cx="6" cy="6" rx="5.5" ry="3.4" transform="rotate(-40 6 6)" fill="none" stroke="var(--sky)" stroke-width="1"/><path d="M4 8 L8 4" stroke="var(--sky)" stroke-width="0.9"/></svg>Recapitalizations</li>
        <li><svg viewBox="0 0 12 12"><ellipse cx="6" cy="6" rx="5.5" ry="3.4" transform="rotate(-40 6 6)" fill="none" stroke="var(--sky)" stroke-width="1"/><path d="M4 8 L8 4" stroke="var(--sky)" stroke-width="0.9"/></svg>Structured Leases</li>
      </ul>

      <div class="band band-products">And our products include:</div>
      <ul class="checklist list-products">
        <li><svg viewBox="0 0 12 12"><path d="M3 1 H9 V4 A3 3 0 0 1 3 4 Z M6 7 V9 M3.5 11 H8.5 L8 9 H4 Z" fill="none" stroke="var(--sky)" stroke-width="1"/></svg>Bridge</li>
        <li><svg viewBox="0 0 12 12"><path d="M3 1 H9 V4 A3 3 0 0 1 3 4 Z M6 7 V9 M3.5 11 H8.5 L8 9 H4 Z" fill="none" stroke="var(--sky)" stroke-width="1"/></svg>Mezzanine</li>
        <li><svg viewBox="0 0 12 12"><path d="M3 1 H9 V4 A3 3 0 0 1 3 4 Z M6 7 V9 M3.5 11 H8.5 L8 9 H4 Z" fill="none" stroke="var(--sky)" stroke-width="1"/></svg>Unitranche</li>
        <li><svg viewBox="0 0 12 12"><path d="M3 1 H9 V4 A3 3 0 0 1 3 4 Z M6 7 V9 M3.5 11 H8.5 L8 9 H4 Z" fill="none" stroke="var(--sky)" stroke-width="1"/></svg>NNN Lease</li>
        <li><svg viewBox="0 0 12 12"><path d="M3 1 H9 V4 A3 3 0 0 1 3 4 Z M6 7 V9 M3.5 11 H8.5 L8 9 H4 Z" fill="none" stroke="var(--sky)" stroke-width="1"/></svg>Preferred Equity</li>
      </ul>
    </section>

    <footer class="brand-footer">
      <span class="brand-square"></span>
      <span class="brand-name">RVB</span>
    </footer>
  </main>
</body>
</html>
```